A tri fold flyer to be sent to parents advertising Learning Center, tutoring in math or language after school and on weekendsSince 1994 the Bright Owl Study House has been helping the children on Oahu do better in school. Bright Owl has developed a successful method of teaching math, reading and writing for students in grades K-12. Affordable and effective, it's unlike any other learning system.

Target Market(s)

Parents of school age kids

Industry/Entity Type

Education

Font styles to use
Sans Serif

Requirements
Must have
• same text as in previews
Nice to have
• 3 fold
Should not have
• mistakes

```html
<!DOCTYPE html>
<html lang="en">
<head>
<meta charset="utf-8">
<title>Bright Owl Hawaii – Tri-fold Flyer</title>
<link rel="stylesheet" href="https://fonts.googleapis.com/css2?family=Jost:wght@400;500;700;800&display=swap">
<style>
  :root {
    --sky: #6fb2e0;
    --sky-deep: #3f8ccc;
    --sky-pale: #dbe9f4;
    --ink: #111111;
    --white: #ffffff;
    --photo-warm: #c9b7a6;
    --photo-board: #2f5a3c;
  }
  * { box-sizing: border-box; margin: 0; padding: 0; }
  html, body { width: 1200px; height: 800px; overflow: hidden; }
  body { font-family: "Jost", sans-serif; background: #e6e6e6; }
  .flyer { display: flex; width: 1200px; height: 800px; }
  .panel { position: relative; width: 400px; height: 800px; overflow: hidden; }

  /* Left panel: testimonials */
  .panel--testimonials { background: linear-gradient(180deg, #8cc3e8 0%, var(--sky) 45%, #5da6da 100%); color: var(--white); }
  .testimonials__photo {
    position: absolute; left: 0; top: 0; width: 400px; height: 250px;
    background: linear-gradient(120deg, var(--photo-board) 0%, #5f8a6a 40%, var(--photo-warm) 75%, #e9e4dc 100%);
  }
  .testimonials__backdrop {
    position: absolute; left: 0; top: 250px; width: 400px; height: 550px;
    background: radial-gradient(ellipse at 40% 40%, rgba(255,255,255,0.18), rgba(255,255,255,0) 70%);
  }
  .testimonials__body { position: absolute; left: 30px; right: 30px; top: 225px; text-align: center; }
  .testimonials__title { font-size: 22px; font-weight: 500; line-height: 1.25; margin-bottom: 18px; }
  .quote { font-size: 17px; line-height: 1.3; margin-bottom: 16px; }

  /* Middle panel: call to action */
  .panel--offer { background: linear-gradient(160deg, #7bbbe6 0%, var(--sky) 50%, #5aa3d8 100%); color: var(--white); text-align: center; }
  .offer__photo {
    position: absolute; inset: 0;
    background: radial-gradient(ellipse at 60% 45%, rgba(240,220,200,0.28), rgba(255,255,255,0) 60%);
  }
  .offer__body { position: absolute; left: 0; right: 0; top: 60px; }
  .offer__lead { font-size: 40px; font-weight: 700; line-height: 1.12; }
  .offer__lead strong { font-weight: 800; }
  .offer__phone { font-size: 44px; font-weight: 700; margin-top: 4px; }
  .offer__alt { font-size: 28px; font-weight: 700; line-height: 1.2; margin-top: 34px; }
  .offer__address { font-size: 20px; font-weight: 500; line-height: 1.35; margin-top: 34px; }

  /* Right panel: cover */
  .panel--cover { background: linear-gradient(180deg, #f3f6f9 0%, var(--sky-pale) 55%, #c7dced 100%); color: var(--ink); text-align: center; }
  .cover__brand { position: absolute; left: 40px; right: 40px; top: 80px; }
  .cover__name { font-size: 46px; font-weight: 500; letter-spacing: 1px; line-height: 1; padding-bottom: 10px; border-bottom: 3px solid var(--ink); }
  .cover__region { font-size: 28px; font-weight: 500; letter-spacing: 10px; margin-top: 10px; }
  .cover__tagline { position: absolute; left: 0; right: 0; top: 240px; }
  .cover__tagline-strong { font-size: 20px; font-weight: 800; }
  .cover__tagline-light { font-size: 20px; font-weight: 400; display: inline-block; padding-bottom: 6px; border-bottom: 1px solid #d98a8a; }
  .cover__photo {
    position: absolute; left: 0; right: 0; top: 390px; height: 410px;
    background: linear-gradient(180deg, rgba(255,255,255,0) 0%, #e7ecf0 30%, #d6cfc8 70%, #c8d6e2 100%);
  }
</style>
</head>
<body>
<main class="flyer">
  <section class="panel panel--testimonials">
    <div class="testimonials__photo" role="img" aria-label="Photo of a tutor and a parent cheering with a happy child in front of a chalkboard"></div>
    <div class="testimonials__backdrop" role="img" aria-label="Faint photo of a child studying, tinted blue"></div>
    <div class="testimonials__body">
      <h2 class="testimonials__title">Bright Owl Works:<br>These are comments from<br>Bright Owl parents:</h2>
      <p class="quote">"My son loves Bright Owl classes; I noticed a big change in him toward his school work."</p>
      <p class="quote">"The 2/1 ratio and individualized support makes the program a success."</p>
      <p class="quote">"The staff at Bright Owl is very helpful, friendly and just super!"</p>
      <p class="quote">"Bright Owl really made my kids look forward to learning new things and to look forward to going to school."</p>
      <p class="quote">"My daughter has improved 90% with school."</p>
      <p class="quote">"We are very pleased with the results. Bright Owl is the best investment I have made for my son!"</p>
    </div>
  </section>

  <section class="panel panel--offer">
    <div class="offer__photo" role="img" aria-label="Photo of a tutor helping a child write, tinted blue"></div>
    <div class="offer__body">
      <p class="offer__lead">For a<br><strong>FREE TEST</strong><br>and a<br><strong>FREE TRIAL<br>LESSON</strong><br>CALL</p>
      <p class="offer__phone">555-0142</p>
      <p class="offer__alt">555-OWLS<br>555-0142</p>
      <p class="offer__address">Harbor View Business Plaza<br>410 Lanakila Way<br>Harbor City HI 96700<br>www.brightowlhawaii.com</p>
    </div>
  </section>

  <section class="panel panel--cover">
    <div class="cover__brand">
      <p class="cover__name">Bright Owl</p>
      <p class="cover__region">HAWAII</p>
    </div>
    <div class="cover__tagline">
      <p class="cover__tagline-strong">MORE THAN</p>
      <p class="cover__tagline-light">JUST TUTORING...</p>
    </div>
    <div class="cover__photo" role="img" aria-label="Photo of a thoughtful young schoolboy resting his chin on his hand while holding a pencil"></div>
  </section>
</main>
</body>
</html>
```